Dietitian needs a new business card design

I need a new business card design for my nutrition business that provides individual clinical nutrition advice for people with medical conditions. Business cards will be handed out to doctors, specialists and clients so will need to be sharp and project an image of professionalism

Target Market(s)

My clients are typically referred by doctors or specialists and the card will be used to handout to clients and their doctors.

Industry/Entity Type

Medical

Contact Information for Business Card

The business card will require the details below. These details can be found from my website https://www.tamberlydietitian.com.au/

Font styles to use
Serif

Colors

Designer to choose colors to be used in the design.

Requirements
Must have
• 1. It needs be professional and contemporary
• 2. It needs to incorporate my logo
• 3. It needs space to write appointment times and dates
• 4. It needs to provide my phone number, fax number, email address and my web address
Nice to have
• Include the Endorsed Clinical Dietitian Logo
• I have access to Pixorra if required
• The locations I practise from
Should not have
• Pictures of food
• Spelling MIstakes

```html
<!DOCTYPE html>
<html lang="en">
<head>
<meta charset="utf-8">
<title>Tamberly Nutrition &amp; Dietetics – Business Card</title>
<link href="https://fonts.googleapis.com/css2?family=Andika:wght@400;700&family=Roboto+Condensed:wght@300;400&display=swap" rel="stylesheet">
<style>
  :root {
    --bg: #e6e8eb;
    --white: #ffffff;
    --navy: #0a5aa8;
    --blue: #0f68b8;
    --sky: #0b9fe3;
    --green: #8cc63f;
    --badge: #f47a20;
    --mist: #c9e6d6;
  }
  * { margin: 0; padding: 0; box-sizing: border-box; }
  html, body { width: 960px; height: 1200px; overflow: hidden; }
  body { background: var(--bg); position: relative; font-family: "Andika", sans-serif; }

  .card {
    position: absolute; left: 55px; width: 852px; height: 487px;
    background: var(--white); overflow: hidden;
    box-shadow: 0 4px 14px rgba(0,0,0,.18);
  }
  .card--front { top: 68px; }
  .card--back { top: 642px; }

  .brand-mark {
    position: absolute; left: 40px; top: 40px; width: 270px; height: 270px;
    border-radius: 50%;
    background: radial-gradient(circle at 35% 35%, #8fb6e0 0%, var(--mist) 55%, #dfeea0 100%);
    display: flex; align-items: center; justify-content: center; text-align: center;
  }
  .brand-mark span { color: var(--navy); font-size: 26px; font-weight: 400; line-height: 1.15; }

  .holder { position: absolute; right: 38px; top: 34px; text-align: right; color: var(--navy); }
  .holder__name { font-size: 52px; font-weight: 700; letter-spacing: .5px; line-height: 1.1; color: var(--blue); }
  .holder__role { font-family: "Roboto Condensed", sans-serif; font-weight: 300; font-size: 25px; margin-top: 4px; }
  .badge { display: inline-block; width: 71px; height: 32px; background: var(--badge); margin-top: 10px; }

  .contact {
    position: absolute; right: 38px; top: 222px; text-align: right;
    font-family: "Roboto Condensed", sans-serif; font-weight: 300; font-size: 22px; color: var(--navy);
  }
  .contact p { line-height: 36px; }
  .contact .label { margin-right: 28px; }
  .contact .label--tight { margin-right: 8px; }

  .services {
    position: absolute; left: 0; top: 358px; width: 100%; height: 78px;
    background: linear-gradient(90deg, var(--blue), var(--sky));
    display: flex; align-items: center; justify-content: flex-end; padding-right: 38px;
    font-family: "Roboto Condensed", sans-serif; font-weight: 300; font-size: 22.5px; color: var(--white);
  }
  .web {
    position: absolute; left: 0; top: 436px; width: 100%; height: 51px;
    display: flex; align-items: center; justify-content: center;
    font-family: "Roboto Condensed", sans-serif; font-weight: 300; font-size: 22.5px; color: var(--navy);
  }

  .appointment {
    position: absolute; left: 0; top: 0; width: 100%; height: 320px;
    background: linear-gradient(100deg, var(--blue) 0%, var(--sky) 100%);
    color: var(--white);
  }
  .appointment__title { position: absolute; top: 30px; width: 100%; text-align: center; font-size: 40px; font-weight: 700; }
  .field { position: absolute; top: 96px; display: flex; align-items: flex-end; font-size: 21px; font-weight: 700; }
  .field--date { left: 54px; }
  .field--time { left: 474px; }
  .field__line { display: inline-block; border-bottom: 2px solid var(--white); margin-left: 12px; height: 22px; }
  .field--date .field__line { width: 290px; }
  .field--time .field__line { width: 278px; }

  .location { position: absolute; }
  .location__name { display: flex; align-items: center; font-size: 24px; font-weight: 700; letter-spacing: .4px; }
  .location__name::before { content: ""; width: 15px; height: 15px; background: var(--white); margin-right: 10px; }
  .location__addr { font-size: 15px; font-weight: 700; margin-top: 6px; }
  .loc-1 { left: 54px; top: 160px; }
  .loc-2 { left: 474px; top: 160px; }
  .loc-3 { left: 54px; top: 243px; }
  .loc-4 { left: 474px; top: 243px; }

  .signoff {
    position: absolute; left: 0; top: 320px; width: 100%; height: 167px;
    display: flex; align-items: center; justify-content: center; gap: 14px;
  }
  .signoff__dot { width: 22px; height: 22px; border-radius: 50%; background: var(--green); }
  .signoff__name { font-size: 34px; font-weight: 400; color: var(--navy); }
</style>
</head>
<body>
  <section class="card card--front">
    <div class="brand-mark"><span>Tamberly<br>Nutrition</span></div>
    <div class="holder">
      <h1 class="holder__name">Daniel Whitcombe</h1>
      <p class="holder__role">Accredited Nutritionist | Qualified Chef</p>
      <span class="badge" role="img" aria-label="Endorsed Clinical Dietitian badge"></span>
    </div>
    <div class="contact">
      <p><span class="label">Phone:</span>0412 555 306</p>
      <p><span class="label label--tight">Fax:</span>+613 6200 4817</p>
      <p>daniel@tamberlydietitian.com.au</p>
    </div>
    <div class="services">Chronic Disease Management Plans | Nutrition Solutions | Corporate Nutrition Consulting</div>
    <div class="web">www.tamberlydietitian.com.au</div>
  </section>

  <section class="card card--back">
    <div class="appointment">
      <h2 class="appointment__title">Appointment</h2>
      <div class="field field--date">Date:<span class="field__line"></span></div>
      <div class="field field--time">Time:<span class="field__line"></span></div>
      <div class="location loc-1"><p class="location__name">Ashgrove Medical Centre</p><p class="location__addr">Cnr Elm &amp; Baxter Streets | Hillcrest</p></div>
      <div class="location loc-2"><p class="location__name">Brookvale Doctors Surgery</p><p class="location__addr">8 Millers Road | Brookvale</p></div>
      <div class="location loc-3"><p class="location__name">Kingsford Medical</p><p class="location__addr">4/161 Harbour Road | Kingsford</p></div>
      <div class="location loc-4"><p class="location__name">East Ridge Health</p><p class="location__addr">7 Wattle Drive | Ridgeway</p></div>
    </div>
    <div class="signoff">
      <span class="signoff__dot"></span>
      <span class="signoff__name">Tamberly Nutrition &amp; Dietetics</span>
    </div>
  </section>
</body>
</html>
```